Waterproofing/Crawlspace wrap

Car Wrap Design Brief

2000 Varlo Box Truck

-Full wrap with your own unique design
-Doors and front looking for a unique logo and decal look
-add QR Code

```html
<!DOCTYPE html>
<html lang="en">
<head>
<meta charset="utf-8">
<title>Marlow's Waterproofing – Box Truck Wrap</title>
<link rel="stylesheet" href="https://fonts.googleapis.com/css2?family=Alfa+Slab+One&family=Oswald:wght@500;600&family=Roboto+Condensed:wght@700&family=Montserrat:wght@600&display=swap">
<style>
  :root{
    --canvas:#eceef1;
    --panel-white:#f7f8fa;
    --panel-edge:#c9ccd2;
    --brand-blue:#1f5fb8;
    --deep-blue:#1b4c9c;
    --sky-blue:#3f9be6;
    --brand-red:#d9453f;
    --title-red:#c9302c;
    --white:#ffffff;
  }
  *{box-sizing:border-box;margin:0;padding:0}
  html,body{width:1200px;height:1200px;overflow:hidden;background:var(--canvas)}
  .canvas{position:relative;width:1200px;height:1200px}

  /* Box side panel */
  .side-panel{position:absolute;left:50px;top:60px;width:1100px;height:560px;background:var(--panel-white);border:8px solid var(--panel-edge);overflow:hidden}
  .estimate-band{position:absolute;left:22px;top:20px;right:22px;height:52px;background:var(--brand-blue);color:var(--white);font:600 30px/52px "Oswald",sans-serif;letter-spacing:1px;padding-left:170px}
  .brand-title{position:absolute;left:22px;width:760px;text-align:center;color:var(--title-red);font-family:"Alfa Slab One",serif}
  .brand-title--name{top:100px;font-size:78px;letter-spacing:5px}
  .brand-title--trade{top:205px;font-size:42px;letter-spacing:6px}
  .contact-bar{position:absolute;left:22px;top:282px;width:760px;height:50px;background:var(--brand-red);color:var(--white);display:flex;align-items:center}
  .contact-bar .phone{font:700 34px/1 "Roboto Condensed",sans-serif;letter-spacing:2px;padding:0 22px 0 36px;border-right:3px solid var(--white)}
  .contact-bar .email{font:600 19px/1 "Montserrat",sans-serif;padding-left:18px}
  .service-block{position:absolute;left:22px;top:332px;right:22px;bottom:20px;background:var(--brand-blue)}
  .service-list{position:absolute;top:352px;list-style:none;color:var(--white);font:700 21px/35px "Roboto Condensed",sans-serif;text-transform:uppercase}
  .service-list li::before{content:"";display:inline-block;width:9px;height:9px;background:var(--white);margin-right:10px;vertical-align:middle}
  .service-list--left{left:62px}
  .service-list--right{left:440px}
  .emblem-area{position:absolute;right:48px;top:40px;width:250px;height:460px;border-radius:24px;border:10px solid var(--white);background:linear-gradient(160deg,var(--sky-blue),var(--deep-blue))}

  /* Front header + cab decal */
  .front-header{position:absolute;left:50px;top:690px;width:520px;height:170px;background:var(--brand-blue);border:8px solid var(--panel-edge);color:var(--white);text-align:center}
  .front-header .phone{font:700 56px/1 "Roboto Condensed",sans-serif;letter-spacing:3px;margin-top:30px}
  .front-header .email{font:600 22px/1 "Montserrat",sans-serif;margin-top:18px}

  .cab-decal{position:absolute;left:630px;top:690px;width:520px;height:170px;background:var(--white);border:8px solid var(--panel-edge);display:flex;flex-direction:column;justify-content:center}
  .cab-decal .mark-row{display:flex;align-items:center;justify-content:center;gap:16px}
  .cab-decal .mark-dot{width:30px;height:30px;border-radius:50%;background:var(--brand-blue)}
  .cab-decal .name{font:44px/1 "Alfa Slab One",serif;color:var(--title-red);letter-spacing:3px}
  .cab-decal .trade{font:20px/1 "Alfa Slab One",serif;color:var(--title-red);letter-spacing:4px;text-align:center;margin-top:10px}
  .cab-decal .stripe{height:12px;background:var(--brand-red);margin-top:18px}

  .cab-body{position:absolute;left:50px;top:900px;width:1100px;height:240px;border:8px solid var(--panel-edge);background:linear-gradient(var(--white) 0 48%,var(--brand-red) 48% 54%,var(--brand-blue) 54% 100%)}
</style>
</head>
<body>
<main class="canvas">
  <section class="side-panel" aria-label="Box side panel">
    <div class="estimate-band">FREE ESTIMATES</div>
    <h1 class="brand-title brand-title--name">MARLOW'S</h1>
    <p class="brand-title brand-title--trade">WATERPROOFING</p>
    <div class="contact-bar">
      <span class="phone">555-014-2867</span>
      <span class="email">marlows.services@example.com</span>
    </div>
    <div class="service-block"></div>
    <ul class="service-list service-list--left">
      <li>Waterproofing Solutions</li>
      <li>Crawl Space Encapsulation</li>
      <li>Crawl Space Waterproofing</li>
      <li>Sump Pump Installation</li>
      <li>Basement Dehumidifier</li>
    </ul>
    <ul class="service-list service-list--right">
      <li>Mold Remediation</li>
      <li>Basement Waterproofing</li>
      <li>Interior/Exterior Drain</li>
      <li>Vapor Barrier</li>
    </ul>
    <div class="emblem-area" role="img" aria-label="Area for the company's large brand emblem in blue tones"></div>
  </section>

  <section class="front-header" aria-label="Front box header">
    <p class="phone">555-014-2867</p>
    <p class="email">marlows.services@example.com</p>
  </section>

  <section class="cab-decal" aria-label="Cab door decal">
    <div class="mark-row">
      <span class="mark-dot"></span>
      <span class="name">MARLOW'S</span>
    </div>
    <p class="trade">WATERPROOFING</p>
    <div class="stripe"></div>
  </section>

  <section class="cab-body" aria-label="Cab colour scheme: white upper, red stripe, blue lower"></section>
</main>
</body>
</html>
```